Mobile grocery convenience store app

PantryVan is a mobile grocery store. Customers should be able to request the grocery bus to their home address. See where the bus is with map and estimated time. Put multiple people requests in order they request. Give an 15 min -20 min per stop for customers to come aboard bus and shops/pay for for their grocery. Must have log in for bus driver/clerk to sign in and see get directions to next address in que and info they would need. Such as contact for customer should driver get lost. Similar to zova and Kemo. Special instructions for handicap so driver can bring items to door. Products we sale should be able to be added or changed easily by manager or sign in.
Updates

Problem starting design contest. Was never supposed to be 6 days. Thanks

Industry/Entity Type

Grocery

Font styles to use
Sans Serif

Colors
0255a3
fee18a
fece3e

Requirements
Must have
• Colors match as close to logo colors

```html
<!DOCTYPE html>
<html lang="en">
<head>
<meta charset="UTF-8">
<title>PantryVan – Log In</title>
<link rel="stylesheet" href="https://fonts.googleapis.com/css2?family=Red+Hat+Display:wght@400;500;700;900&display=swap">
<style>
  :root {
    --brand-blue: #0255a3;
    --deep-blue: #084a8c;
    --ghost-blue: #0a4d93;
    --sun-yellow: #fece3e;
    --soft-yellow: #fee18a;
    --navy: #1c2a6e;
    --orange: #f5a31f;
    --white: #ffffff;
    --ink: #2b2b2b;
    --ui-font: "Red Hat Display", "Helvetica Neue", Arial, sans-serif;
  }
  * { box-sizing: border-box; margin: 0; padding: 0; }
  html, body { width: 675px; height: 1200px; overflow: hidden; background: var(--brand-blue); }
  .screen {
    position: relative; width: 675px; height: 1200px; overflow: hidden;
    background: var(--brand-blue); font-family: var(--ui-font);
  }
  .backdrop { position: absolute; inset: 0; }
  .status-bar {
    position: absolute; top: 0; left: 0; right: 0; height: 40px;
    display: flex; justify-content: space-between; align-items: center;
    padding: 0 14px; z-index: 3;
  }
  .status-time { font-size: 17px; font-weight: 500; color: #000; letter-spacing: 0.2px; }
  .brand-block {
    position: absolute; left: 162px; top: 108px; width: 351px;
    display: flex; flex-direction: column; align-items: center;
  }
  .brand-dot { width: 96px; height: 96px; border-radius: 50%; background: var(--orange); }
  .brand-name {
    margin-top: 32px; font-size: 52px; font-weight: 700; color: var(--navy);
    letter-spacing: -0.5px; line-height: 1;
  }
  .ghost-title {
    position: absolute; left: 0; right: 0; top: 528px; text-align: center;
    font-size: 178px; font-weight: 900; color: var(--ghost-blue); line-height: 1;
    letter-spacing: 4px; white-space: nowrap; opacity: 0.85;
  }
  .screen-title {
    position: absolute; left: 0; right: 0; top: 584px; text-align: center;
    font-size: 58px; font-weight: 900; color: var(--white); letter-spacing: -1px; line-height: 1;
  }
  .login-form { position: absolute; left: 84px; top: 700px; width: 508px; }
  .field {
    display: flex; align-items: center; justify-content: space-between;
    height: 74px; border-radius: 37px; background: var(--white);
    padding: 0 30px 0 37px; margin-bottom: 30px;
    font-size: 17px; color: var(--ink); font-weight: 400;
  }
  .field svg { width: 20px; height: 22px; fill: #333; }
  .actions { display: flex; justify-content: space-between; margin-top: 6px; }
  .btn {
    width: 238px; height: 74px; border-radius: 37px; border: none;
    font-family: var(--ui-font); font-size: 23px; font-weight: 900; letter-spacing: -0.3px;
    color: var(--white); display: flex; align-items: center; justify-content: center;
    box-shadow: 0 8px 16px rgba(0, 30, 70, 0.25);
  }
  .btn-login { background: var(--sun-yellow); }
  .btn-signin { background: var(--deep-blue); }
  .social-links {
    position: absolute; left: 0; right: 0; top: 1027px;
    display: flex; justify-content: center; gap: 23px;
  }
  .social-link {
    width: 68px; height: 68px; border-radius: 50%; background: var(--deep-blue);
    display: flex; align-items: center; justify-content: center;
    color: var(--white); font-size: 11px; font-weight: 700;
  }
</style>
</head>
<body>
<main class="screen">
  <svg class="backdrop" width="675" height="1200" viewBox="0 0 675 1200" aria-hidden="true">
    <defs>
      <linearGradient id="top-fade" x1="0" y1="0" x2="0" y2="1">
        <stop offset="0" stop-color="#ffffff"/>
        <stop offset="0.05" stop-color="#ffffff"/>
        <stop offset="0.2" stop-color="#fee18a"/>
        <stop offset="0.32" stop-color="#fece3e"/>
        <stop offset="1" stop-color="#fece3e"/>
      </linearGradient>
    </defs>
    <path class="wave-left" fill="#084a8c" d="M0,560 C70,510 210,520 248,620 C282,705 232,780 170,845 C90,930 -5,1030 10,1200 L0,1200 Z"/>
    <path class="wave-bottom" fill="#084a8c" d="M100,1017 C190,1105 310,1140 410,1112 C500,1085 560,962 675,958 L675,1200 L240,1200 C180,1135 135,1075 100,1017 Z"/>
    <circle class="ring" cx="337.5" cy="126" r="385" fill="url(#top-fade)"/>
    <circle class="badge" cx="337.5" cy="126" r="301" fill="#ffffff"/>
  </svg>

  <header class="status-bar">
    <span class="status-time">9:41</span>
    <svg width="108" height="18" viewBox="0 0 108 18" aria-label="Signal, Wi-Fi and battery">
      <rect x="0" y="11" width="3.5" height="5" rx="1" fill="#000"/>
      <rect x="5.5" y="8" width="3.5" height="8" rx="1" fill="#000"/>
      <rect x="11" y="5" width="3.5" height="11" rx="1" fill="#000"/>
      <rect x="16.5" y="2" width="3.5" height="14" rx="1" fill="#000"/>
      <path d="M38,5 a13,13 0 0 1 18,0 l-2,2.2 a10,10 0 0 0 -14,0 Z M41,9 a8,8 0 0 1 12,0 l-2,2.2 a5,5 0 0 0 -8,0 Z M44.5,13 a3,3 0 0 1 5,0 L47,16 Z" fill="#000"/>
      <rect x="68" y="2" width="30" height="14" rx="4" fill="none" stroke="#000" stroke-width="1.4"/>
      <rect x="70.5" y="4.5" width="25" height="9" rx="2" fill="#000"/>
      <rect x="99.5" y="6.5" width="2" height="5" rx="1" fill="#000"/>
    </svg>
  </header>

  <section class="brand-block">
    <div class="brand-dot"></div>
    <h2 class="brand-name">PantryVan</h2>
  </section>

  <div class="ghost-title" aria-hidden="true">LOG IN</div>
  <h1 class="screen-title">LOG IN</h1>

  <form class="login-form">
    <div class="field">
      <span>Name</span>
      <svg viewBox="0 0 20 22" aria-hidden="true"><circle cx="10" cy="6" r="5"/><path d="M1,21 C1,14 5,12.5 10,12.5 C15,12.5 19,14 19,21 Z"/></svg>
    </div>
    <div class="field">
      <span>Password</span>
      <svg viewBox="0 0 20 22" aria-hidden="true"><path d="M5,9 V6.5 a5,5 0 0 1 10,0 V9 H12.6 V6.5 a2.6,2.6 0 0 0 -5.2,0 V9 Z"/><rect x="2.5" y="9" width="15" height="12.5" rx="1.5"/><circle cx="10" cy="14.5" r="1.6" fill="#fff"/></svg>
    </div>
    <div class="actions">
      <span class="btn btn-login">LOG IN</span>
      <span class="btn btn-signin">SIGN IN</span>
    </div>
  </form>

  <nav class="social-links">
    <span class="social-link">Kinnect</span>
    <span class="social-link">Chirpa</span>
  </nav>
</main>
</body>
</html>
```